Marlo Tidy Yard Website

We need a website design for this new company. I've attached the company logo. This company is in the construction industry that provides general labor, maintenance and cleaning for construction sites. We want a clean and simple website that can be easy to navigate.

Target Market(s)

Construction industry

Industry/Entity Type

Construction

Number of Pages Required

2 page

Font styles to use
Sans Serif

```html
<!DOCTYPE html>
<html lang="en">
<head>
<meta charset="utf-8">
<title>Marlo Tidy Yard</title>
<link href="https://fonts.googleapis.com/css2?family=Open+Sans:wght@300;400;600;700&display=swap" rel="stylesheet">
<style>
:root{
  --accent:#f2b200;
  --dark:#2e2e2e;
  --darker:#242424;
  --panel:#3a3a3a;
  --ink:#333;
  --muted:#888;
  --line:#e3e3e3;
  --paper:#fff;
  --soft:#f4f4f4;
  --brand:#1f3d8c;
}
*{box-sizing:border-box;margin:0;padding:0}
html,body{width:1200px;height:3529px;overflow:hidden}
body{font-family:"Open Sans",Arial,sans-serif;color:var(--ink);background:var(--paper);position:relative;font-size:11px}
.band{position:absolute;left:0;width:1200px}
.wrap{position:absolute;left:242px;width:714px}
.section-title{position:absolute;left:242px;width:714px;height:28px;font-size:16px;font-weight:600;color:var(--ink);border-bottom:1px solid var(--line);line-height:18px}
.section-title::after{content:"";position:absolute;left:0;bottom:-1px;width:40px;height:3px;background:var(--accent)}
.band .section-title{color:#fff;border-color:#4a4a4a}
.more-link{position:absolute;font-size:9px;color:var(--muted);display:flex;align-items:center;gap:6px;justify-content:flex-end}
.more-link::before{content:"";width:6px;height:6px;border-radius:50%;background:var(--accent)}
.rule{position:absolute;left:242px;width:714px;height:1px;background:var(--line)}

/* top bar */
.topbar{top:0;height:26px;background:var(--darker);color:#aaa;font-size:9px}
.topbar .info{position:absolute;left:482px;top:7px;display:flex;gap:24px;white-space:nowrap}
.social{position:absolute;display:flex;gap:12px}
.social span{width:10px;height:10px;border-radius:50%;background:#777;display:block}

/* header */
.header{top:26px;height:54px;background:#fff;border-bottom:1px solid var(--line)}
.logo{position:absolute;display:flex;align-items:center;gap:8px;font-weight:700;font-size:15px;color:var(--brand);white-space:nowrap}
.logo i{width:18px;height:18px;background:var(--brand);display:block}
.nav{position:absolute;left:546px;top:21px;display:flex;gap:26px;font-size:9px;font-weight:600;color:#555;letter-spacing:.5px;white-space:nowrap}

/* hero */
.hero{top:80px;height:390px;background:linear-gradient(180deg,#6f8296 0%,#9fb0bd 35%,#8a7a62 62%,#6b4e33 100%)}
.hero-title{position:absolute;left:0;width:1200px;top:118px;text-align:center;color:#fff;font-weight:300;font-size:34px;letter-spacing:2px}
.hero-text{position:absolute;left:360px;width:480px;top:172px;text-align:center;color:#fff;font-size:13px;line-height:20px}
.hero-btns{position:absolute;top:222px;left:0;width:1200px;display:flex;justify-content:center;gap:18px}
.btn{height:30px;padding:0 18px;display:flex;align-items:center;font-size:9px;font-weight:700;letter-spacing:.5px}
.btn-accent{background:var(--accent);color:#fff}
.btn-ghost{border:1px solid #fff;color:#fff}
.btn-line{border:1px solid #ccc;color:#666}
.hero-arrow{position:absolute;top:168px;width:24px;height:30px;background:rgba(0,0,0,.45)}
.hero-arrow svg{display:block;margin:9px auto}

/* quick links */
.quick{top:470px;height:83px;background:var(--dark)}
.quick .wrap{top:0;height:75px;display:flex}
.quick-item{flex:1;background:var(--panel);border-right:1px solid #4a4a4a;padding:20px 20px 0}
.quick-item:last-child{border:0}
.quick-item h3{font-size:13px;font-weight:400;color:#fff;display:flex;justify-content:space-between}
.quick-item p{font-size:8px;color:#888;margin-top:12px}

/* services */
.cards{top:682px;display:flex;gap:25px}
.card{width:160px;height:264px;border:1px solid #ddd;box-shadow:0 0 0 3px #f1f1f1;background:#fff;position:relative}
.card .media{height:115px;margin:3px}
.card h4{font-size:10px;font-weight:600;margin:12px 10px 6px}
.card p{font-size:8px;color:var(--muted);line-height:12px;margin:0 10px}
.card .read{position:absolute;bottom:0;left:0;right:0;height:30px;border-top:1px solid var(--line);font-size:8px;color:#666;display:flex;justify-content:space-between;align-items:center;padding:0 10px}

/* projects */
.projects{top:1061px;height:593px;background:var(--dark)}
.filters{position:absolute;top:28px;left:0;width:1200px;display:flex;justify-content:center;gap:4px}
.filters span{font-size:8px;color:#aaa;border:1px solid #555;padding:5px 10px}
.filters span.on{background:var(--accent);color:#222;border-color:var(--accent)}
.grid{position:absolute;top:66px;left:0;width:1200px;display:grid;grid-template-columns:repeat(3,1fr);grid-template-rows:236px 236px}
.all-projects{position:absolute;top:556px;width:1200px;text-align:center;color:var(--accent);font-size:10px;font-weight:700}

/* about */
.about-text{position:absolute;left:242px;top:1753px;width:330px;font-size:10px;line-height:15px;color:#777}
.about-btns{position:absolute;left:242px;top:1835px;display:flex;gap:8px}
.about-media{position:absolute;left:588px;top:1725px;width:368px;height:169px;clip-path:polygon(22% 0,100% 0,100% 100%,0 100%)}

/* reasons */
.reason-grid{top:2007px;display:grid;grid-template-columns:repeat(3,1fr);gap:21px 18px}
.reason{height:87px;border:1px solid #ddd;padding:18px 12px;display:flex;gap:10px}
.reason i{width:18px;height:18px;background:#eee;display:block;flex:none}
.reason h4{font-size:10px;font-weight:600;margin-bottom:6px}
.reason p{font-size:8px;color:var(--muted);line-height:11px}

/* news */
.gap-band{top:2281px;height:18px;background:var(--soft)}
.news{top:2299px;height:494px;background:var(--dark)}
.pager{position:absolute;display:flex;gap:3px}
.pager span{width:22px;height:22px;border:1px solid #555;display:flex;align-items:center;justify-content:center}
.news-cards{position:absolute;left:242px;top:129px;display:flex;gap:20px}
.post{width:225px;height:294px;background:#fff;border:3px solid #ddd;position:relative}
.post .media{height:145px;position:relative}
.post .date{position:absolute;left:8px;top:8px;width:26px;height:30px;background:#fff;font-size:9px;font-weight:700;text-align:center;line-height:12px;padding-top:3px}
.post .date small{display:block;font-size:7px;font-weight:400;color:#888}
.post h4{font-size:11px;font-weight:600;margin:14px 12px;line-height:15px}
.post .read{position:absolute;bottom:0;left:0;right:0;height:30px;border-top:1px solid var(--line);font-size:8px;color:#666;display:flex;justify-content:space-between;align-items:center;padding:0 12px}

/* testimonials */
.quote-row{top:2953px;display:flex;gap:20px}
.quote{width:347px;display:flex;gap:12px}
.quote .who{width:80px;text-align:center;padding-top:18px}
.quote .who i{width:40px;height:40px;border-radius:50%;display:block;margin:0 auto 6px;background:#a89a86}
.quote .who b{font-size:8px;font-weight:600;display:block}
.quote .who small{font-size:7px;color:#999}
.quote blockquote{flex:1;height:106px;border:3px solid #e6e6e6;padding:12px;font-size:9px;line-height:13px;color:#888;font-style:italic}

/* call to action */
.cta{top:3165px;height:80px;background:var(--soft);text-align:center;line-height:80px;font-size:12px;font-weight:600}

/* footer */
.footer{top:3247px;height:282px;background:var(--darker);color:#999}
.footer .col{position:absolute;top:50px;font-size:8px;line-height:15px;white-space:nowrap}
.footer .col h5{font-size:10px;color:#ddd;font-weight:600;margin-bottom:10px}
.footer .logo{left:242px;top:150px;color:#fff;font-size:16px}
.inquiry{position:absolute;left:730px;top:160px;width:226px;height:30px;border:1px solid #555;color:#ccc;font-size:8px;display:flex;align-items:center;justify-content:center;letter-spacing:.5px}
.footer .bottom{position:absolute;left:0;top:240px;width:1200px;height:42px;border-top:1px solid #3a3a3a}
</style>
</head>
<body>

<div class="band topbar">
  <div class="info">
    <span>Working time: Mon-Fri 08:00 - 18:00</span>
    <span>Email: info@marlotidyyard.com</span>
    <span>Phone: +1 555 014 2290</span>
  </div>
  <div class="social" style="left:890px;top:8px"><span></span><span></span><span></span><span></span></div>
</div>

<header class="band header">
  <div class="logo" style="left:40px;top:18px"><i></i>Marlo Tidy Yard</div>
  <nav class="nav"><span>HOME ▾</span><span>SERVICES ▾</span><span>PROJECTS</span><span>ABOUT US ▾</span><span>BLOG</span><span>SHOP</span><span>CONTACT US</span></nav>
</header>

<section class="band hero" role="img" aria-label="Excavator arm digging soil on a construction site under a cloudy sky">
  <div class="hero-arrow" style="left:12px"><svg width="8" height="12"><path d="M6 1L2 6l4 5" stroke="#fff" fill="none" stroke-width="1.5"/></svg></div>
  <div class="hero-arrow" style="right:12px"><svg width="8" height="12"><path d="M2 1l4 5-4 5" stroke="#fff" fill="none" stroke-width="1.5"/></svg></div>
  <h1 class="hero-title">MODERN MACHINERY</h1>
  <p class="hero-text">We work for the highest standards in the industry. This helps us not only stay ahead of the competition, but to offer the best solutions to our clients.</p>
  <div class="hero-btns"><span class="btn btn-accent">GET A QUOTE</span><span class="btn btn-ghost">LEARN MORE</span></div>
</section>

<section class="band quick">
  <div class="wrap">
    <div class="quick-item"><h3>Our Work <span>›</span></h3><p>See what we have been working on</p></div>
    <div class="quick-item"><h3>All Services <span>›</span></h3><p>See all services</p></div>
    <div class="quick-item"><h3>Free Quote <span>›</span></h3><p>Want to discuss a project? Click here</p></div>
  </div>
</section>

<h2 class="section-title" style="top:620px">Our services</h2>
<div class="wrap cards">
  <article class="card"><div class="media" role="img" aria-label="Loader tipping soil into a truck" style="background:linear-gradient(#c9b58a,#a07a3e)"></div><h4>Machine rent</h4><p>Lorem ipsum dolor sit amet, consectetur adipiscing elit. Quisque nec erat sed, quisque nec erat.</p><div class="read">READ MORE <span>›</span></div></article>
  <article class="card"><div class="media" role="img" aria-label="Yellow crane on a building site" style="background:linear-gradient(#cfd6dc,#b39a42)"></div><h4>Construction</h4><p>Lorem ipsum dolor sit amet, consectetur adipiscing elit. Quisque nec erat sed, quisque nec erat.</p><div class="read">READ MORE <span>›</span></div></article>
  <article class="card"><div class="media" role="img" aria-label="Bulldozer preparing a site" style="background:linear-gradient(#d8c6a3,#8c6a3a)"></div><h4>Site preparation</h4><p>Lorem ipsum dolor sit amet, consectetur adipiscing elit. Quisque nec erat sed, quisque nec erat.</p><div class="read">READ MORE <span>›</span></div></article>
  <article class="card"><div class="media" role="img" aria-label="Excavator working on open ground" style="background:linear-gradient(#8fb4d6,#c9a24a)"></div><h4>Engineering</h4><p>Lorem ipsum dolor sit amet, consectetur adipiscing elit. Quisque nec erat sed, quisque nec erat.</p><div class="read">READ MORE <span>›</span></div></article>
</div>
<div class="rule" style="top:976px"></div>
<div class="more-link" style="left:242px;width:714px;top:986px">All Services</div>

<section class="band projects">
  <div class="filters"><span class="on">All Projects</span><span>Residential</span><span>Shopping</span><span>Office</span><span>Commercial</span></div>
  <div class="grid">
    <div role="img" aria-label="Glass and steel canopy roof" style="background:linear-gradient(135deg,#8fa3b4,#dfe6ec)"></div>
    <div role="img" aria-label="Glazed corridor around an inner garden" style="background:linear-gradient(180deg,#e6e4df,#b6ab98)"></div>
    <div role="img" aria-label="Modern glass office facade" style="background:linear-gradient(135deg,#f0f2f3,#7f8f9a)"></div>
    <div role="img" aria-label="Building with glass balconies" style="background:linear-gradient(180deg,#7c8590,#3f4549)"></div>
    <div role="img" aria-label="Small house lit at dusk" style="background:linear-gradient(180deg,#5e6a77,#2f2a25)"></div>
    <div role="img" aria-label="Bright interior with dining table and stairs" style="background:linear-gradient(135deg,#f3f3f2,#c9c4bf)"></div>
  </div>
  <div class="all-projects">ALL PROJECTS ›</div>
</section>

<h2 class="section-title" style="top:1707px;width:330px">About Marlo Tidy Yard</h2>
<p class="about-text">Lorem ipsum is simply dummy text of the printing and typesetting industry. Lorem ipsum has been the industry's standard dummy text ever since the 1500s, when an unknown printer took a galley of type and scrambled it to make a type specimen book. It has survived not only five centuries.</p>
<div class="about-btns"><span class="btn btn-line">READ MORE</span><span class="btn btn-accent">CAREERS</span></div>
<div class="about-media" role="img" aria-label="Glazed interior corridor" style="background:linear-gradient(135deg,#bfb8aa,#f0efec 60%,#9a8f7c)"></div>

<h2 class="section-title" style="top:1958px">6 Reasons to Choose us</h2>
<div class="wrap reason-grid">
  <div class="reason"><i></i><div><h4>Full service package</h4><p>Lorem ipsum dolor sit amet, consectetur adipiscing elit quisque nec erat sed.</p></div></div>
  <div class="reason"><i></i><div><h4>Great Talent</h4><p>Lorem ipsum dolor sit amet, consectetur adipiscing elit quisque nec erat sed.</p></div></div>
  <div class="reason"><i></i><div><h4>Time-Sensitive Planning</h4><p>Lorem ipsum dolor sit amet, consectetur adipiscing elit quisque nec erat sed.</p></div></div>
  <div class="reason"><i></i><div><h4>Eco Engineering</h4><p>Lorem ipsum dolor sit amet, consectetur adipiscing elit quisque nec erat sed.</p></div></div>
  <div class="reason"><i></i><div><h4>New Technologies</h4><p>Lorem ipsum dolor sit amet, consectetur adipiscing elit quisque nec erat sed.</p></div></div>
  <div class="reason"><i></i><div><h4>30 year warranty</h4><p>Lorem ipsum dolor sit amet, consectetur adipiscing elit quisque nec erat sed.</p></div></div>
</div>

<div class="band gap-band"></div>

<section class="band news">
  <h2 class="section-title" style="top:68px">Latest News</h2>
  <div class="pager" style="left:910px;top:66px"><span><svg width="6" height="9"><path d="M5 1L1 4.5 5 8" stroke="#888" fill="none"/></svg></span><span><svg width="6" height="9"><path d="M1 1l4 3.5L1 8" stroke="#888" fill="none"/></svg></span></div>
  <div class="news-cards">
    <article class="post"><div class="media" role="img" aria-label="White interior with staircase" style="background:linear-gradient(135deg,#eee,#9c958c)"><span class="date">20<small>Jun</small></span></div><h4>The Harbor Lofts has reached its final stage of construction (4)</h4><div class="read">READ MORE <span>›</span></div></article>
    <article class="post"><div class="media" role="img" aria-label="Rows of workshop machines" style="background:linear-gradient(180deg,#6d6356,#2f2a24)"><span class="date">18<small>Jun</small></span></div><h4>New machines dramatically increase our productivity (3)</h4><div class="read">READ MORE <span>›</span></div></article>
    <article class="post"><div class="media" role="img" aria-label="Hands shaping wet clay" style="background:linear-gradient(135deg,#c89a76,#7a5a45)"><span class="date">16<small>Jun</small></span></div><h4>Case study: How we increased electricity efficiency by 46% (12)</h4><div class="read">READ MORE <span>›</span></div></article>
  </div>
  <div class="more-link" style="left:242px;width:714px;top:462px">All Articles</div>
</section>

<h2 class="section-title" style="top:2896px">Testimonials</h2>
<div class="pager" style="left:910px;top:2893px"><span style="border-color:#ddd"><svg width="6" height="9"><path d="M5 1L1 4.5 5 8" stroke="#999" fill="none"/></svg></span><span style="border-color:#ddd"><svg width="6" height="9"><path d="M1 1l4 3.5L1 8" stroke="#999" fill="none"/></svg></span></div>
<div class="wrap quote-row">
  <div class="quote"><div class="who"><i role="img" aria-label="Client portrait"></i><b>Alan Reeve</b><small>Business Office, Ltd</small></div><blockquote>Marlo Tidy Yard is a really professional team. They kept us informed throughout the whole process of building our bedroom house. We got suggestions on what materials to choose, the timeframe and price went.</blockquote></div>
  <div class="quote"><div class="who"><i role="img" aria-label="Client portrait"></i><b>Ruth Calder</b><small>Business Office, Ltd</small></div><blockquote>Marlo Tidy Yard is a really professional team. They kept us informed throughout the whole process of building our bedroom house. We got suggestions on what materials to choose, the timeframe and price went.</blockquote></div>
</div>
<div class="rule" style="top:3087px"></div>
<div class="more-link" style="left:242px;width:714px;top:3097px">All Testimonials</div>

<section class="band cta">Get a Free Quote for Your Project. Click Here ›</section>

<footer class="band footer">
  <div class="col" style="left:242px"><h5>Useful Information</h5>How to save on your Next Home Project<br>10 Top Ingredients for a Perfect House Renovation<br>5 Stories on Huge Renovation Savings<br>Best Tools for a Renovation in 2016</div>
  <div class="col" style="left:487px"><h5>Pages</h5>Portfolio<br>Services<br>Contact us<br>Get free quote<br>Privacy Policy<br>Shop</div>
  <div class="col" style="left:607px"><h5>About</h5>Careers<br>T&amp;C<br>Privacy Policy<br>Management<br>News</div>
  <div class="col" style="left:730px"><h5>Contact Details</h5>Phone: +1 555 014 2290<br>Email: info@marlotidyyard.com<br>Address: 48 Fenwick Row, Dallas</div>
  <div class="logo"><i></i>Marlo Tidy Yard</div>
  <div class="inquiry">SEND AN INQUIRY</div>
  <div class="bottom"><div class="social" style="left:878px;top:15px"><span></span><span></span><span></span><span></span></div></div>
</footer>

</body>
</html>
```